Insurance Firm needs Stationary and Corporate Identity

We have a logo (provided) - we need a business card, letterhead, booklet cover, Benefit & Travel card design, and brand guide.
KTR (Kestrel Trust Reinsurers) is a National (Canadian) family-run benefits firm. We've been providing alternative benefit models to small and medium sized businesses for almost 25 years! Our goal is to create long-lasting customer relationships by partnering with our clients to become their dedicated benefits division instead of just selling a product to them.

Benefit & Travel Cards: We provide the benefit card to employees to allow them to pay for drugs at their pharmacy and dental services electronically.
The travel card is for medical emergencies while travelling outside of Canada.

Brand Guide: Once the stationary is complete, the brand guide will allow us to streamline the use of our logo's and fonts for internal and external use. We will expect that this will be a paid project for our design winner after the contest closes and we will negotiate the pricetag for this at that time.

Target Market(s)

Business Owners, Entrepreneurs, HR Professionals

Industry/Entity Type

Insurance Agency

Font styles to use
Sans Serif

Requirements
Must have
• business card, letterhead, health card, travel card, booklet cover (some current samples provided)

```html
<!DOCTYPE html>
<html lang="en">
<head>
<meta charset="utf-8">
<title>Kestrel Trust Reinsurers — Stationery</title>
<link rel="stylesheet" href="https://fonts.googleapis.com/css2?family=Didact+Gothic&family=Roboto:wght@400;500&display=swap">
<style>
:root{
  --bg:#e2e2e2;
  --paper:#f4f4f4;
  --paper-edge:#ececec;
  --grey:#77797d;
  --grey-light:#b3b4b6;
  --red:#d8232a;
  --ink:#3a3a3a;
  --ink-soft:#5a5a5a;
  --sig:#8fa3c8;
}
*{margin:0;padding:0;box-sizing:border-box}
html,body{width:1200px;height:993px;overflow:hidden;background:var(--bg)}
body{position:relative;font-family:"Didact Gothic",sans-serif;color:var(--ink)}

.brand{display:flex;flex-direction:column;align-items:center;gap:6px;white-space:nowrap}
.brand-row{display:flex;align-items:center;gap:8px}
.brand-dot{border-radius:50%;background:var(--red)}
.brand-name{font-family:"Roboto",sans-serif;font-weight:500;color:var(--grey);letter-spacing:1px;line-height:1}
.brand-full{font-family:"Roboto",sans-serif;font-weight:500;color:var(--grey);letter-spacing:.4px;line-height:1}

.contact{font-family:"Roboto",sans-serif;font-size:9px;line-height:11px;color:var(--ink-soft);white-space:nowrap}
.contact .addr{margin-bottom:4px}
.contact li{list-style:none;display:flex;align-items:center;gap:5px}
.contact svg{width:8px;height:8px;fill:var(--red);flex:none}

/* Letterhead */
.letterhead{position:absolute;left:452px;top:79px;width:596px;height:836px;
  background:linear-gradient(180deg,var(--paper),var(--paper-edge));box-shadow:0 2px 10px rgba(0,0,0,.12)}
.letterhead .brand{position:absolute;left:17px;top:60px;width:180px}
.letterhead .brand-name{font-size:44px}
.letterhead .brand-dot{width:14px;height:14px}
.letterhead .brand-full{font-size:10px}
.letterhead .contact{position:absolute;left:446px;top:62px}
.greeting{position:absolute;left:56px;top:223px;font-size:15px;color:var(--ink)}
.letter-body{position:absolute;left:56px;top:266px;width:492px}
.letter-body p{font-size:8.9px;line-height:12.7px;color:var(--ink-soft);margin-bottom:12.7px}
.closing{position:absolute;left:56px;top:530px;font-size:8.5px;color:var(--ink-soft)}
.signature{position:absolute;left:56px;top:579px;width:102px;height:50px;
  background:linear-gradient(90deg,rgba(143,163,200,.25),rgba(143,163,200,.12));border-radius:4px}
.sheet-footer{position:absolute;left:0;bottom:0;width:100%;height:26px}
.footer-url{position:absolute;left:0;right:0;bottom:11px;text-align:center;font-family:"Roboto",sans-serif;
  font-size:8.5px;letter-spacing:4px;color:#fff}

/* Business cards */
.card{position:absolute;left:67px;width:322px;height:184px;box-shadow:0 2px 8px rgba(0,0,0,.14)}
.card-front{top:508px;background:var(--paper)}
.card-back{top:729px;background:var(--grey);display:flex;align-items:center;justify-content:center}
.card-front .brand{position:absolute;left:10px;top:56px;width:180px}
.card-front .brand-name{font-size:36px}
.card-front .brand-dot{width:12px;height:12px}
.card-front .brand-full{font-size:9px}
.card-divider{position:absolute;left:175px;top:43px;width:1px;height:92px;background:var(--grey-light)}
.person{position:absolute;left:191px;top:42px}
.person-name{font-family:"Roboto",sans-serif;font-weight:500;font-size:11px;color:var(--red)}
.person-role{font-family:"Roboto",sans-serif;font-size:8px;color:var(--grey);margin-bottom:9px}
.card-front .contact{font-size:8px;line-height:10.5px}
.card-footer{position:absolute;left:0;bottom:0;width:100%;height:14px}
.card-url{position:absolute;left:0;right:0;bottom:2px;text-align:center;font-family:"Roboto",sans-serif;
  font-size:7.5px;letter-spacing:3px;color:#fff}
.card-back .brand{gap:8px}
.card-back .brand-name{font-size:42px;color:#fff}
.card-back .brand-dot{width:13px;height:13px}
.card-back .brand-full{font-size:10px;color:#fff}
</style>
</head>
<body>

<svg width="0" height="0" style="position:absolute">
  <defs>
    <symbol id="i-phone" viewBox="0 0 10 10"><path d="M2 0.5l2 2-1 1.2a6 6 0 0 0 3.3 3.3l1.2-1 2 2-1.3 1.5C4.5 9.3 0.7 5.5 0.5 1.8z"/></symbol>
    <symbol id="i-mobile" viewBox="0 0 10 10"><path d="M2.5 0h5v10h-5zM3.5 1v7h3V1z"/></symbol>
    <symbol id="i-fax" viewBox="0 0 10 10"><path d="M2.5 0h5v3h-5zM0 3.5h10v4.5H8V6H2v2H0zM2.5 6.5h5V10h-5z"/></symbol>
    <symbol id="i-mail" viewBox="0 0 10 10"><path d="M0 2h10v1L5 6 0 3zM0 4l5 3 5-3v4H0z"/></symbol>
  </defs>
</svg>

<article class="letterhead">
  <div class="brand">
    <div class="brand-row"><span class="brand-dot"></span><span class="brand-name">KTR</span></div>
    <span class="brand-full">KESTREL TRUST REINSURERS</span>
  </div>
  <div class="contact">
    <div class="addr">412 Larchmont Way<br>Halifax, Nova Scotia 20917</div>
    <ul>
      <li><svg><use href="#i-phone"/></svg>902 555 0148</li>
      <li><svg><use href="#i-mobile"/></svg>902 555 0173</li>
      <li><svg><use href="#i-fax"/></svg>902 555 0196</li>
      <li><svg><use href="#i-mail"/></svg>name@ktr-mail.ca</li>
    </ul>
  </div>

  <div class="greeting">Dear Ms. Quinn,</div>
  <div class="letter-body">
    <p>Lorem ipsum dolor sit amet, consectetur adipiscing elit. Donec orci purus, luctus vitae dignissim eu, iaculis sed purus. Vivamus faucibus, ipsum nec aliquet viverra, leo mauris condimentum ligula, sit amet sagittis enim ligula quis arcu. Nam egestas tortor id nisi porttitor mattis. In tortor ante, ultricies in suscipit a, tempus non massa. Vivamus et auctor mi. Fusce vel massa nulla. Phasellus nec eros mauris, et scelerisque orci.</p>
    <p>Donec malesuada orci vitae nulla accumsan porta a id massa. Quisque accumsan iaculis magna sit amet fringilla. Maecenas consequat, magna eget tincidunt semper, odio nibh rutrum mi, id feugiat ante nisi eu risus. Vestibulum nunc orci, rhoncus a placerat in, ultricies in mi. Cras mattis varius eros, vel fringilla nisi suscipit eget. Quisque scelerisque sagittis nulla at porttitor.</p>
    <p>Sed id augue vitae urna euismod commodo aliquet a quam. Pellentesque arcu velit, cursus et malesuada ut, consequat et diam. Nullam erat sem, rhoncus id ullamcorper vitae, rhoncus et arcu. In ultricies ultricies nulla, ut rutrum nisi iaculis at. Donec eu magna a metus ornare faucibus. Fusce aliquet faucibus ultricies. Morbi semper, est id tincidunt gravida, sem arcu adipiscing lacus, ac bibendum nulla leo eu purus. Quisque nec diam sed risus consectetur accumsan quis quis nibh. Vestibulum id purus lorem.</p>
    <p>It is a long established fact that a reader will be distracted by the readable content of a page when looking at its layout. The point of using Lorem Ipsum is that it has a more-or-less normal distribution of letters, as opposed to using 'Content here, content here', making it look like readable English. Many desktop publishing packages</p>
  </div>
  <div class="closing">Sincerely,</div>
  <div class="signature" role="img" aria-label="Handwritten signature in blue ink"></div>

  <svg class="sheet-footer" viewBox="0 0 596 26" preserveAspectRatio="none">
    <rect x="0" y="8" width="94" height="8" fill="var(--red)"/>
    <rect x="94" y="8" width="100" height="8" fill="var(--grey-light)"/>
    <rect x="402" y="8" width="100" height="8" fill="var(--grey-light)"/>
    <rect x="502" y="8" width="94" height="8" fill="var(--red)"/>
    <rect x="0" y="16" width="596" height="10" fill="var(--grey)"/>
    <path d="M193 16 L210 2 Q213 0 218 0 H378 Q383 0 386 2 L403 16 Z" fill="var(--grey)"/>
  </svg>
  <div class="footer-url">www.ktr-mail.ca</div>
</article>

<section class="card card-front">
  <div class="brand">
    <div class="brand-row"><span class="brand-dot"></span><span class="brand-name">KTR</span></div>
    <span class="brand-full">KESTREL TRUST REINSURERS</span>
  </div>
  <div class="card-divider"></div>
  <div class="person">
    <div class="person-name">MARLA QUINN</div>
    <div class="person-role">CEO/FOUNDER</div>
    <div class="contact">
      <div class="addr">412 Larchmont Way<br>Halifax, Nova Scotia 20917</div>
      <ul>
        <li><svg><use href="#i-phone"/></svg>902 555 0148</li>
        <li><svg><use href="#i-mobile"/></svg>902 555 0173</li>
        <li><svg><use href="#i-fax"/></svg>902 555 0196</li>
        <li><svg><use href="#i-mail"/></svg>name@ktr-mail.ca</li>
      </ul>
    </div>
  </div>
  <svg class="card-footer" viewBox="0 0 322 14" preserveAspectRatio="none">
    <rect x="0" y="5" width="51" height="5" fill="var(--red)"/>
    <rect x="51" y="5" width="54" height="5" fill="var(--grey-light)"/>
    <rect x="217" y="5" width="54" height="5" fill="var(--grey-light)"/>
    <rect x="271" y="5" width="51" height="5" fill="var(--red)"/>
    <path d="M104 14 L113 2 Q115 0 118 0 H204 Q207 0 209 2 L218 14 Z" fill="var(--grey)"/>
  </svg>
  <div class="card-url">www.ktr-mail.ca</div>
</section>

<section class="card card-back">
  <div class="brand">
    <div class="brand-row"><span class="brand-dot"></span><span class="brand-name">KTR</span></div>
    <span class="brand-full">KESTREL TRUST REINSURERS</span>
  </div>
</section>

</body>
</html>
```